business card Kalvorin

Wee need a business card design for a new compagny based on Paris
We developped innovative a platform for selling services to refresh, beautify and develop its housing.
We would like a red logo on a black background
Te final design should communicate quality service, know-how, high-end

Target Market(s)

individuals

Industry/Entity Type

Business

```html
<!DOCTYPE html>
<html lang="en">
<head>
<meta charset="utf-8">
<title>Kalvorin — Business Card</title>
<link rel="stylesheet" href="https://fonts.googleapis.com/css2?family=Questrial&family=Montserrat:wght@700&family=Open+Sans:wght@400;600&display=swap">
<style>
  :root {
    --backdrop: #e4e4e4;
    --card-black: #0c0c0d;
    --card-black-soft: #1d1d1f;
    --coral: #e86a64;
    --coral-deep: #d9554f;
    --silver: #9a9a9a;
    --silver-light: #c4c4c4;
    --wordmark: #a8a8a8;
    --white: #ffffff;
  }
  * { box-sizing: border-box; margin: 0; padding: 0; }
  html, body { width: 1200px; height: 852px; overflow: hidden; }
  body {
    background: var(--backdrop);
    position: relative;
    font-family: "Open Sans", sans-serif;
  }
  .card {
    position: absolute;
    width: 500px;
    height: 286px;
    border-radius: 22px;
    overflow: hidden;
    background: linear-gradient(135deg, var(--card-black-soft) 0%, var(--card-black) 55%, #050505 100%);
    box-shadow: 0 14px 28px rgba(0,0,0,0.28);
  }
  .card--front { left: 80px; top: 283px; }
  .card--back { left: 620px; top: 283px; }

  .brand {
    position: absolute;
    display: flex;
    align-items: center;
    gap: 12px;
  }
  .brand__square {
    width: 58px; height: 58px;
    background: var(--coral);
  }
  .brand__name {
    font-family: "Questrial", sans-serif;
    font-size: 52px;
    line-height: 1;
    color: var(--wordmark);
    letter-spacing: 0.5px;
  }
  .card--front .brand { left: 96px; top: 114px; }
  .card--back .brand { left: 34px; top: 40px; }
  .card--back .brand__square { width: 54px; height: 54px; }
  .card--back .brand__name { font-size: 48px; }

  .person { position: absolute; left: 36px; top: 138px; }
  .person__name {
    font-family: "Montserrat", sans-serif;
    font-weight: 700;
    font-size: 17px;
    color: var(--coral);
  }
  .person__role {
    font-size: 12px;
    color: var(--white);
    margin-top: 2px;
  }

  .card__swoosh { position: absolute; inset: 0; width: 500px; height: 286px; }

  .contact {
    position: absolute;
    right: 16px;
    top: 94px;
    list-style: none;
    text-align: right;
    color: var(--white);
    font-size: 11.5px;
    line-height: 17px;
  }
  .contact li { display: flex; justify-content: flex-end; align-items: center; gap: 6px; }
  .contact svg { width: 11px; height: 11px; flex: none; }
</style>
</head>
<body>

  <section class="card card--front" aria-label="Card front">
    <div class="brand">
      <div class="brand__square"></div>
      <span class="brand__name">Kalvorin</span>
    </div>
  </section>

  <section class="card card--back" aria-label="Card back">
    <svg class="card__swoosh" viewBox="0 0 500 286" aria-hidden="true">
      <path d="M500,46 C420,92 388,176 296,214 C220,246 140,250 100,262 L100,270 C150,262 226,258 300,228 C392,190 430,108 500,66 Z" fill="var(--silver)"/>
      <path d="M500,74 C424,116 390,196 300,236 C230,266 150,266 112,286 L500,286 Z" fill="var(--coral)"/>
      <path d="M500,60 C426,104 394,184 300,224 C230,254 150,258 106,274 L108,280 C156,266 234,264 304,232 C396,192 432,114 500,72 Z" fill="var(--silver-light)"/>
    </svg>

    <div class="brand">
      <div class="brand__square"></div>
      <span class="brand__name">Kalvorin</span>
    </div>

    <div class="person">
      <p class="person__name">Your Long Name</p>
      <p class="person__role">Managing Director</p>
    </div>

    <ul class="contact">
      <li>00.00.00.0000
        <svg viewBox="0 0 12 12"><path d="M2 3h8l-1 2H3z M3 6h6v4H3z" fill="var(--white)"/></svg>
      </li>
      <li>00.00.00.0000
        <svg viewBox="0 0 12 12"><rect x="2" y="1" width="8" height="4" fill="none" stroke="var(--white)"/><rect x="1" y="5" width="10" height="6" fill="var(--white)"/></svg>
      </li>
      <li>www.yourwebsite.com
        <svg viewBox="0 0 12 12"><circle cx="6" cy="6" r="4.5" fill="none" stroke="var(--white)"/><path d="M1.5 6h9M6 1.5v9" stroke="var(--white)"/></svg>
      </li>
      <li>yourname@yourwebsite.com
        <svg viewBox="0 0 12 12"><rect x="1" y="3" width="10" height="7" fill="var(--white)"/><path d="M1 3l5 4 5-4" fill="none" stroke="var(--coral)"/></svg>
      </li>
      <li>Your Commercial or office address
        <svg viewBox="0 0 12 12"><path d="M6 11C3 7 2.5 5.5 2.5 4.5a3.5 3.5 0 0 1 7 0C9.5 5.5 9 7 6 11z" fill="var(--white)"/><circle cx="6" cy="4.5" r="1.2" fill="var(--coral)"/></svg>
      </li>
    </ul>
  </section>

</body>
</html>
```